Book cover for a very impressive real-life healing story from a stage IV deadly disease

I need a book cover design for the French translation of the US book http://www.pagevendo.com/Tims-Journey-Fever-Outlasted-Illness/dp/0845512097/ref=sr_1_4?s=books&ie=UTF8&qid=1455100794&sr=1-4&keywords=kit+marsh
.
I do not want the word AIDS on the French cover, as the story of this book applies to any disease.

The french title will be something like :
Un nouveau matin !
Condamné par la médecine, il guérit grâce au jeûne, la détoxination, et l’amour.

which means something like
A new morning!
Subtitle : Given up by official medecine, he managed to heal with fasting, detox and love.

Many thanks !

Target Market(s)

Anybody interested in natural health

Requirements
Must have
• Nothing special
Nice to have
• Nothing special
Should not have
• Nothing special

```html
<!DOCTYPE html>
<html lang="fr">
<head>
<meta charset="utf-8">
<title>Un nouveau matin ! — Kit Marsh</title>
<link rel="stylesheet" href="https://fonts.googleapis.com/css2?family=Anton&family=Oswald:wght@600&family=Arimo&display=swap">
<style>
  :root {
    --ink: #000000;
    --title-red: #d4252b;
    --paper-white: #ffffff;
    --tone-dusk: #3a3432;
    --tone-red: #a3321f;
    --tone-orange: #d9561f;
    --tone-night: #0a0808;
  }
  html, body {
    margin: 0;
    padding: 0;
    width: 750px;
    height: 1200px;
    overflow: hidden;
    background: var(--ink);
  }
  .cover {
    position: relative;
    width: 750px;
    height: 1200px;
    background: var(--ink);
    overflow: hidden;
  }
  .cover-title {
    position: absolute;
    left: 0;
    top: 0;
    width: 750px;
    height: 500px;
  }
  .cover-title text {
    font-family: "Anton", "Oswald", sans-serif;
    fill: var(--title-red);
  }
  .cover-subtitle {
    position: absolute;
    left: 565px;
    top: 294px;
    margin: 0;
    font-family: "Oswald", "Arial Narrow", sans-serif;
    font-weight: 600;
    font-size: 20px;
    line-height: 32.5px;
    color: var(--paper-white);
    text-transform: uppercase;
    letter-spacing: -0.3px;
  }
  .title-rule {
    position: absolute;
    left: 0;
    top: 524px;
    width: 750px;
    height: 8px;
    background: var(--title-red);
  }
  .cover-author {
    position: absolute;
    left: 42px;
    top: 548px;
    margin: 0;
    font-family: "Arimo", "Arial", sans-serif;
    font-weight: 400;
    font-size: 41px;
    color: var(--paper-white);
  }
  .cover-photo {
    position: absolute;
    left: 0;
    top: 600px;
    width: 750px;
    height: 600px;
    background: linear-gradient(to bottom,
      var(--ink) 0%,
      var(--tone-dusk) 12%,
      var(--tone-red) 25%,
      var(--tone-orange) 40%,
      var(--tone-red) 50%,
      var(--tone-night) 62%,
      var(--ink) 100%);
  }
</style>
</head>
<body>
  <main class="cover">
    <svg class="cover-title" viewBox="0 0 750 500" role="heading" aria-level="1" aria-label="Un nouveau matin !">
      <text x="48" y="253" font-size="218" textLength="660" lengthAdjust="spacingAndGlyphs">UN NOUVEAU</text>
      <text x="48" y="485" font-size="218" textLength="482" lengthAdjust="spacingAndGlyphs">MATIN !</text>
    </svg>
    <p class="cover-subtitle">Condamné par<br>la médecine, il<br>guérit grâce<br>au jeûne,<br>la détoxination,<br>et l’amour</p>
    <div class="title-rule"></div>
    <p class="cover-author">Kit Marsh</p>
    <div class="cover-photo" role="img" aria-label="Photograph of a sunrise over a dark, flat landscape under a red and orange sky"></div>
  </main>
</body>
</html>
```